New Web-Page Design Required

We need a new or initial web design for our page varno-labs.com. We provide products & services around infrastructure products. We have two products at the moment, but another 2 in the pipeline.
We want to have the following page structure (and part of the project is to design the 7 pages):
- Home
- Products
-One page per product
- Service
- Support
- About
- Contact (Email form)
The start page should include the following information:
- plain circle / Linkedin Links
- Telephone / Email or in general contact details
- News
- Maybe a link-box, where we can highlight/showcase things
- Link to our support portal, quite prominent
- Testimonials
It would be nice if the product pages would have a image header, where we can put up a screenshot or something. Links to datasheet and videos of the product would be nice as well.
We like the "big banner in the middle" designs, like these two Joomla examples. No need to copy them, it should just give you an idea.
http://www.plumeforge.com/itempreview/185
http://www.plumeforge.com/content/asj42/index.php
Budget for images available, so please use placeholders or ask us for specific photos/images, if you need them for your design.
Target Market(s)
Business-2-Business, Decision makers and Technical Leads
Industry/Entity Type
News
Look and feel
Each slider illustrates characteristics of the customer's brand and the style your logo design should communicate.

```html
<!DOCTYPE html>
<html lang="en">
<head>
<meta charset="utf-8">
<title>Contact Us – Varno-Labs</title>
<link href="https://fonts.googleapis.com/css2?family=Josefin+Sans:wght@300;400&family=Arimo:wght@400&display=swap" rel="stylesheet">
<style>
  :root {
    --teal: #1a95b0;
    --ink: #3d4148;
    --muted: #8a8d91;
    --field-border: #c9cbcd;
    --tweet-band: #3a414c;
    --footer-band: #2f353e;
    --icon-grey: #8d9094;
    --white: #ffffff;
  }
  * { box-sizing: border-box; margin: 0; padding: 0; }
  html, body { width: 1200px; height: 585px; overflow: hidden; background: var(--white); }
  body { position: relative; font-family: "Arimo", Arial, sans-serif; }

  .site-header {
    position: absolute; left: 0; top: 0; width: 1200px; height: 78px;
    background: linear-gradient(#ffffff, #f3f3f3);
    box-shadow: 0 2px 5px rgba(0,0,0,.12);
  }
  .brand {
    position: absolute; left: 187px; top: 19px; display: flex; align-items: center; gap: 8px;
    font-family: "Josefin Sans", sans-serif; font-weight: 400; font-size: 27px; color: var(--ink);
    text-decoration: none;
  }
  .brand-dot { width: 35px; height: 35px; border-radius: 50%; background: var(--teal); }
  .brand-name { padding-top: 6px; letter-spacing: -0.3px; }

  .main-nav {
    position: absolute; right: 187px; top: 34px; display: flex;
    font-family: "Josefin Sans", sans-serif; font-size: 15px; color: var(--ink);
  }
  .main-nav a { color: inherit; text-decoration: none; }
  .main-nav a.is-current { color: var(--teal); }
  .main-nav .sep { color: #c3c5c7; margin: 0 12px; }

  .page-title {
    position: absolute; left: 187px; top: 112px;
    font-family: "Josefin Sans", sans-serif; font-weight: 400; font-size: 19px; color: var(--ink);
  }
  .intro { position: absolute; left: 187px; top: 164px; font-size: 10px; color: var(--muted); letter-spacing: .3px; }
  .contact-list { position: absolute; left: 187px; top: 202px; list-style: none; font-size: 10px; letter-spacing: .3px; }
  .contact-list li { height: 24px; display: flex; }
  .contact-list .label { width: 96px; color: var(--muted); }
  .contact-list .value { color: var(--teal); }

  .field {
    position: absolute; border: 1px solid var(--field-border); border-radius: 2px;
    background: linear-gradient(#f0f0f0, #ffffff);
    font-family: "Arimo", Arial, sans-serif; font-size: 10px; color: var(--muted);
    padding: 11px 9px; letter-spacing: .3px;
  }
  .field-name { left: 599px; top: 165px; width: 203px; height: 32px; }
  .field-email { left: 810px; top: 165px; width: 203px; height: 32px; }
  .field-message { left: 599px; top: 206px; width: 414px; height: 99px; padding-top: 10px; }
  .field-message .grip { position: absolute; right: 5px; bottom: 3px; color: #777; font-size: 9px; }

  .send-button {
    position: absolute; left: 600px; top: 314px; width: 119px; height: 33px;
    background: #c9c9c9; border: 1px solid #b8b8b8; padding: 3px 4px;
  }
  .send-button span {
    display: block; height: 100%; background: #4a4b4d; color: var(--white);
    font-size: 14px; text-align: center; line-height: 25px; border: 1px solid #777;
  }

  .tweet-band {
    position: absolute; left: 0; top: 388px; width: 1200px; height: 123px; background: var(--tweet-band);
    font-family: "Josefin Sans", sans-serif; font-weight: 300; color: var(--white); text-align: center;
  }
  .tweet-heading {
    position: absolute; left: 0; right: 0; top: 21px; display: flex; justify-content: center; align-items: center; gap: 11px;
    font-size: 19px; font-weight: 400;
  }
  .tweet-heading .mark { width: 22px; height: 22px; border-radius: 50%; background: var(--white); }
  .tweet-text { position: absolute; left: 0; right: 0; top: 57px; font-size: 18px; }
  .tweet-text .accent { color: var(--teal); }
  .tweet-media { position: absolute; left: 0; right: 0; top: 82px; font-size: 18px; display: flex; justify-content: center; align-items: center; gap: 6px; }

  .site-footer {
    position: absolute; left: 0; top: 511px; width: 1200px; height: 74px; background: var(--footer-band);
    color: var(--white); font-size: 10px; letter-spacing: .4px;
  }
  .footer-info { position: absolute; left: 186px; top: 22px; line-height: 18px; }
  .footer-info .accent { color: var(--teal); }
  .social-links { position: absolute; left: 837px; top: 22px; display: flex; gap: 4px; list-style: none; }
  .social-links li { width: 26px; height: 26px; border-radius: 50%; background: var(--icon-grey); }
  .social-links li.mail { display: flex; align-items: center; justify-content: center; }
</style>
</head>
<body>
  <header class="site-header">
    <a class="brand" href="#"><span class="brand-dot"></span><span class="brand-name">varno·labs</span></a>
    <nav class="main-nav">
      <a href="#">Home</a><span class="sep">/</span>
      <a href="#">Our Products</a><span class="sep">/</span>
      <a href="#">Our Service</a><span class="sep">/</span>
      <a href="#">Support</a><span class="sep">/</span>
      <a href="#">About Us</a><span class="sep">/</span>
      <a href="#" class="is-current">Contact Us</a>
    </nav>
  </header>

  <main>
    <h1 class="page-title">Contact Us</h1>
    <p class="intro">Please do not hesitate to get in contact with us:</p>
    <ul class="contact-list">
      <li><span class="label">General Enquiries:</span><span class="value">info@varno-labs.com</span></li>
      <li><span class="label">Technical Support:</span><span class="value">support@varno-labs.com</span></li>
      <li><span class="label">Product Questions:</span><span class="value">sales@varno-labs.com</span></li>
    </ul>

    <form class="contact-form">
      <div class="field field-name">Your Name...</div>
      <div class="field field-email">Your E-mail</div>
      <div class="field field-message">Your Message<span class="grip">.:i</span></div>
      <div class="send-button"><span>Send Now</span></div>
    </form>
  </main>

  <section class="tweet-band">
    <h2 class="tweet-heading"><span class="mark"></span>Tweets</h2>
    <p class="tweet-text"><span class="accent">Varno-Labs</span> @varnolabs <span class="accent">k.Ledger Video:</span> vl.link/Qm7RtPz2aKe</p>
    <p class="tweet-media">
      <svg width="16" height="11" viewBox="0 0 16 11" aria-hidden="true"><rect width="16" height="11" fill="#1a95b0"/><path d="M6 2.5 L11 5.5 L6 8.5Z" fill="#3a414c"/></svg>
      View media
    </p>
  </section>

  <footer class="site-footer">
    <div class="footer-info">
      <div>Info@varno-labs.com</div>
      <div>Copyright © 2013 <span class="accent">Varno-Labs</span></div>
    </div>
    <ul class="social-links">
      <li></li><li></li><li></li><li></li><li></li>
      <li class="mail">
        <svg width="16" height="11" viewBox="0 0 16 11" aria-hidden="true"><rect x="0.5" y="0.5" width="15" height="10" fill="#2f353e"/><path d="M1 1 L8 6.5 L15 1" stroke="#8d9094" stroke-width="1.4" fill="none"/></svg>
      </li>
    </ul>
  </footer>
</body>
</html>
```